Bright Fern Series- Face & Body Oil Label

Hi,
I need a label design for a new brand- "Bright Fern Series". Modern and expensive looking. Any color scheme. Feel free to be creative! (I'm not set on the brand name above... I was also thinking maybe "TIRA" or "PuraLume".
-Packaging: 4oz / 118mL clear glass "boston round" bottle with a white treatment pump. The product is an oil so it has a golden tint.
-Product: 4oz Biotin & Marula Face & Body Oil (note that the featured ingredients will change. Others will be "Rosehip & Vitamin E", "Lavender & Hemp Seed Oil", "Coconut Oil & Vitamin C"
-Label size: 5" x 2.5" rounded corners
-Main Highlight: "Moisturizing & Healing"
-Other Highlights:
-----non-greasy
-----all-natural
-----paraben-free
-----vegan
(feel free to use icon symbols)
-Ingredient deck attached
-Other info:
----made in Los Angeles, CA
----manufactured by Willowmere Labs LLC
----UPC
The main thing here is the logo and textures to the label. I can fill in / rearrange the info after.
Thank you,
Owen

```html
<!DOCTYPE html>
<html lang="en">
<head>
<meta charset="utf-8">
<title>Bright Fern Series – Biotin &amp; Marula Face &amp; Body Oil Label</title>
<link rel="stylesheet" href="https://fonts.googleapis.com/css2?family=Montserrat:wght@200;300;400&display=swap">
<style>
  :root {
    --canvas: #ffffff;
    --label-blush: #eee2e0;
    --label-edge: #e6d8d6;
    --band-white: #f8f5f7;
    --headline-white: #f9f6f8;
    --mauve-text: #a69190;
    --mauve-soft: #b9a6a6;
  }
  * { box-sizing: border-box; margin: 0; padding: 0; }
  html, body {
    width: 900px;
    height: 1200px;
    overflow: hidden;
    background: var(--canvas);
  }
  .canvas {
    position: relative;
    width: 900px;
    height: 1200px;
    font-family: "Montserrat", sans-serif;
  }
  .label {
    position: absolute;
    left: 170px;
    top: 150px;
    width: 560px;
    height: 900px;
    border-radius: 36px;
    background: linear-gradient(180deg, var(--label-blush) 0%, #f0e6e5 60%, #eee3e3 100%);
    border: 1px solid var(--label-edge);
    overflow: hidden;
  }
  .brand {
    position: absolute;
    left: 120px;
    top: 120px;
    display: flex;
    align-items: center;
    gap: 14px;
    color: var(--mauve-text);
    font-weight: 300;
    font-size: 30px;
    letter-spacing: 0.04em;
    white-space: nowrap;
  }
  .brand-dot {
    width: 14px;
    height: 14px;
    border-radius: 50%;
    background: var(--mauve-soft);
  }
  .side-band {
    position: absolute;
    left: 44px;
    top: 240px;
    width: 22px;
    height: 590px;
    background: var(--band-white);
  }
  .product-type {
    position: absolute;
    left: 82px;
    top: 420px;
    transform-origin: left top;
    transform: rotate(-90deg) translateX(-100%);
    color: var(--mauve-soft);
    font-size: 15px;
    font-weight: 400;
    letter-spacing: 0.14em;
    white-space: nowrap;
  }
  .headline {
    position: absolute;
    left: 112px;
    top: 200px;
    color: var(--headline-white);
    font-weight: 200;
    font-size: 108px;
    line-height: 1.0;
    letter-spacing: -0.01em;
    white-space: nowrap;
  }
  .headline span { display: block; }
  .highlights {
    position: absolute;
    left: 120px;
    top: 470px;
    list-style: none;
    color: var(--mauve-text);
    font-size: 24px;
    font-weight: 400;
    letter-spacing: 0.02em;
    line-height: 1.75;
    white-space: nowrap;
  }
  .highlights .main-highlight { letter-spacing: 0.01em; }
  .net-weight {
    position: absolute;
    right: 130px;
    top: 740px;
    color: var(--mauve-soft);
    font-size: 30px;
    font-weight: 300;
  }
</style>
</head>
<body>
<main class="canvas">
  <section class="label" aria-label="Face and body oil label">
    <div class="brand"><span class="brand-dot"></span>Bright Fern Series</div>
    <div class="side-band"></div>
    <div class="product-type">FACE &amp; BODY OIL</div>
    <h1 class="headline"><span>biotin &amp;</span><span>marula</span></h1>
    <ul class="highlights">
      <li class="main-highlight">MOISTURIZING &amp; HEALING</li>
      <li>NON-GREASY</li>
      <li>PARABEN-FREE</li>
      <li>VEGAN</li>
    </ul>
    <div class="net-weight">4 oz</div>
  </section>
</main>
</body>
</html>
```